Dane Calloway Photography

Would like the Business card to have a cool logo. I’m targeting wedding/ engagement: portrait photography. My phone number on it. And my business email address.

Target Market(s)

Wedding/portrait/engagement photography.

```html
<!DOCTYPE html>
<html lang="en">
<head>
<meta charset="utf-8">
<title>Dane Calloway Photography – Business Card</title>
<link rel="stylesheet" href="https://fonts.googleapis.com/css2?family=Lato:wght@300;400&display=swap">
<style>
  :root {
    --backdrop: #111010;
    --card: #272625;
    --card-edge: #1c1b1a;
    --ink-light: #dcd9d6;
    --ink-muted: #a9a5a1;
    --copper: #c98062;
  }
  * { margin: 0; padding: 0; box-sizing: border-box; }
  html, body {
    width: 1200px;
    height: 900px;
    overflow: hidden;
    background: var(--backdrop);
    font-family: "Lato", sans-serif;
  }
  .stage {
    width: 1200px;
    height: 900px;
    display: flex;
    align-items: center;
    justify-content: center;
    gap: 40px;
  }
  .card {
    position: relative;
    width: 525px;
    height: 300px;
    background: var(--card);
    border-radius: 16px;
    box-shadow: 0 0 0 1px var(--card-edge), 0 18px 40px rgba(0, 0, 0, 0.55);
  }

  /* Front side */
  .card-front .brand {
    position: absolute;
    left: 0;
    right: 0;
    top: 34px;
    display: flex;
    flex-direction: column;
    align-items: center;
    color: var(--ink-light);
    font-weight: 400;
  }
  .card-front .brand-ring {
    width: 58px;
    height: 58px;
    border: 2px solid var(--copper);
    border-radius: 50%;
    margin-bottom: 16px;
  }
  .card-front .brand-name {
    font-size: 31px;
    letter-spacing: 0.3em;
    margin-right: -0.3em;
    line-height: 1;
  }
  .card-front .brand-tag {
    margin-top: 10px;
    font-size: 14px;
    letter-spacing: 0.62em;
    margin-right: -0.62em;
    color: var(--ink-muted);
  }
  .card-front .contact {
    position: absolute;
    left: 62px;
    top: 208px;
    list-style: none;
    color: var(--ink-muted);
    font-size: 16px;
    font-weight: 300;
    line-height: 1.6;
  }
  .card-front .contact li:first-child { padding-left: 70px; }

  /* Back side */
  .card-back {
    display: flex;
    align-items: center;
    justify-content: center;
  }
  .card-back .brand {
    display: flex;
    align-items: center;
    gap: 26px;
  }
  .card-back .brand-ring {
    width: 150px;
    height: 150px;
    border: 3px solid var(--copper);
    border-radius: 50%;
    flex: none;
  }
  .card-back .brand-text {
    color: var(--ink-light);
    font-weight: 400;
    font-size: 20px;
    letter-spacing: 0.26em;
    line-height: 1.7;
  }
</style>
</head>
<body>
  <main class="stage">
    <section class="card card-front" aria-label="Business card front">
      <div class="brand">
        <span class="brand-ring"></span>
        <span class="brand-name">DANE CALLOWAY</span>
        <span class="brand-tag">PHOTOGRAPHY</span>
      </div>
      <ul class="contact">
        <li>t: 030 555 0142</li>
        <li>m: danecalloway@email.com</li>
      </ul>
    </section>

    <section class="card card-back" aria-label="Business card back">
      <div class="brand">
        <span class="brand-ring"></span>
        <span class="brand-text">DANE CALLOWAY<br>PHOTOGRAPHY</span>
      </div>
    </section>
  </main>
</body>
</html>
```